Propose a revamped landing page

One template we like eg is https://www.trovask.com but but cluttered Our logo and colors are attached to our logo and colors are printed on a white background what we have. So font usage ...
1 page

```html
<!DOCTYPE html>
<html lang="de">
<head>
<meta charset="utf-8">
<title>Voltwise – Automatisch zum günstigsten Energieanbieter</title>
<link href="https://fonts.googleapis.com/css2?family=Roboto:wght@400;500;700&display=swap" rel="stylesheet">
<style>
  :root{
    --orange:#f7a823;
    --orange-deep:#f26a22;
    --ink:#3d4450;
    --muted:#6b717a;
    --line:#e9eaec;
    --footer:#40454d;
    --white:#ffffff;
    --sky:#cdeef3;
    --teal:#2fb3a5;
  }
  *{box-sizing:border-box;margin:0;padding:0}
  html,body{width:1200px;height:2908px;overflow:hidden}
  body{font-family:"Roboto",Arial,sans-serif;color:var(--ink);background:var(--white);position:relative}
  .abs{position:absolute}
  .accent{color:var(--orange)}
  .btn{position:absolute;display:inline-block;border-radius:22px;background:linear-gradient(90deg,var(--orange),var(--orange-deep));color:var(--white);font-size:12px;font-weight:700;text-align:center;line-height:42px;height:42px;width:150px;text-decoration:none;box-shadow:0 6px 14px rgba(242,106,34,.3)}
  .rule{position:absolute;height:3px;width:150px;background:var(--orange)}

  /* header */
  .hero{position:absolute;left:0;top:0;width:1200px;height:555px;background:var(--orange)}
  .world-map{position:absolute;left:240px;top:300px;width:720px;height:200px;background:radial-gradient(ellipse at center,rgba(255,255,255,.22),rgba(255,255,255,0) 70%)}
  .brand{position:absolute;font-weight:700;color:var(--white);font-size:28px;letter-spacing:.5px;display:flex;align-items:center;gap:8px}
  .brand .dot{width:14px;height:14px;border-radius:50%;background:var(--white)}
  .nav{position:absolute;top:40px;left:385px;display:flex;gap:36px;font-size:13px;font-weight:500;color:var(--white)}
  .nav a{color:inherit;text-decoration:none;position:relative}
  .nav a.active::after{content:"";position:absolute;left:50%;top:24px;width:6px;height:6px;margin-left:-3px;border-radius:50%;background:var(--orange-deep)}
  .hero h1{position:absolute;top:210px;left:0;width:1200px;text-align:center;font-size:33px;line-height:48px;font-weight:700;color:var(--ink)}
  .hero h1 .hl{color:var(--white)}
  .known{position:absolute;top:470px;width:1200px;text-align:center;font-size:11px;font-weight:500;color:var(--white);letter-spacing:.5px}
  .press{position:absolute;left:150px;top:505px;width:900px;height:102px;background:var(--white);border-radius:4px;box-shadow:0 8px 24px rgba(0,0,0,.08)}
  .press .badge{position:absolute;height:18px;border-radius:3px;background:#b7babf}

  /* intro */
  h2{font-size:27px;line-height:38px;font-weight:700;color:var(--ink)}
  .copy{font-size:12px;line-height:21px;color:var(--muted)}
  .copy p{margin-bottom:18px}
  .copy strong{color:var(--ink)}
  .illus{position:absolute}
  .savings ul{list-style:none}
  .savings li{position:relative;padding-left:16px;font-size:12px;line-height:30px;color:var(--muted)}
  .savings li::before{content:"";position:absolute;left:0;top:12px;width:6px;height:6px;border-radius:50%;background:var(--orange-deep)}
  .savings li strong{color:var(--ink)}
  .note{font-size:8px;line-height:13px;color:#9a9ea5}

  .center-title{position:absolute;left:0;width:1200px;text-align:center}
  .step{position:absolute;top:1875px;width:285px;height:145px;background:var(--white);box-shadow:0 6px 22px rgba(0,0,0,.08);padding:22px 22px}
  .step .num{position:absolute;left:20px;top:12px;font-size:46px;font-weight:700;color:var(--orange)}
  .step h3{margin-left:52px;font-size:14px;line-height:20px;font-weight:500;color:var(--ink)}
  .step p{margin-top:18px;font-size:12px;line-height:20px;color:var(--muted)}
  .steps-map{position:absolute;left:150px;top:1850px;width:900px;height:230px;background:radial-gradient(ellipse at center,rgba(247,168,35,.10),rgba(247,168,35,0) 70%)}

  .feature{position:absolute;top:2295px;width:220px}
  .feature h4{margin-top:30px;font-size:13px;font-weight:700;color:var(--ink);letter-spacing:.3px}
  .feature p{margin-top:12px;font-size:12px;line-height:21px;color:var(--muted)}

  .cta{position:absolute;left:0;top:2620px;width:1200px;height:80px;background:linear-gradient(90deg,var(--orange),var(--orange-deep));display:flex;align-items:center;justify-content:center;gap:30px;color:var(--white);font-size:14px;font-weight:700}
  .cta a{background:var(--white);color:var(--ink);border-radius:22px;height:42px;line-height:42px;width:150px;text-align:center;font-size:12px;text-decoration:none}
  .footer{position:absolute;left:0;top:2700px;width:1200px;height:208px;background:var(--footer)}
  .footer .nav{top:52px}
  .footer .nav a.active{color:var(--orange)}
  .social{position:absolute;left:152px;top:148px;display:flex;gap:12px}
  .social span{width:11px;height:11px;border-radius:50%;background:var(--white)}
  .legal{position:absolute;right:150px;top:145px;font-size:11px;font-weight:500;color:var(--white);word-spacing:4px}
</style>
</head>
<body>

<header class="hero">
  <div class="world-map" role="img" aria-label="Dezente Weltkarte aus Punkten"></div>
  <div class="brand" style="left:150px;top:28px">Voltwise <span class="dot"></span></div>
  <nav class="nav">
    <a class="active" href="#">So Funktionierts</a><a href="#">Preise</a><a href="#">Fragen?</a><a href="#">Über Uns</a><a href="#">Betriebe</a><a href="#">Erfahrungen</a><a href="#">Pressestimmen</a>
  </nav>
  <h1>Immer <span class="hl">automatisch</span> zum <span class="hl">günstigsten</span><br>Energieanbieter wechseln</h1>
  <a class="btn" href="#" style="left:525px;top:337px">Jetzt Anmelden!</a>
  <div class="known">BEKANNT AUS</div>
</header>

<div class="press" aria-label="Medienberichte">
  <div class="badge" style="left:60px;top:20px;width:44px;height:62px;border-radius:50%"></div>
  <div class="badge" style="left:138px;top:24px;width:150px"></div>
  <div class="badge" style="left:345px;top:24px;width:118px"></div>
  <div class="badge" style="left:525px;top:24px;width:128px"></div>
  <div class="badge" style="left:710px;top:24px;width:136px"></div>
  <div class="badge" style="left:138px;top:60px;width:96px"></div>
  <div class="badge" style="left:292px;top:60px;width:96px"></div>
  <div class="badge" style="left:438px;top:60px;width:114px"></div>
  <div class="badge" style="left:585px;top:60px;width:140px"></div>
  <div class="badge" style="left:775px;top:60px;width:64px"></div>
</div>

<section class="intro">
  <h2 class="abs" style="left:150px;top:718px">Nie wieder <span class="accent">zu viel</span> für<br>Strom &amp; Gas bezahlen</h2>
  <div class="rule" style="left:150px;top:808px"></div>
  <div class="copy abs" style="left:150px;top:852px;width:440px">
    <p>Vorbei sind die Zeiten von schlechten Deals, mühsamem Tarifvergleich und langweiligen Wechselformularen.</p>
    <p>Mit dem automatischen Wechselservice für Voltwise wirst du nie wieder zu viel für Strom und Gas bezahlen. Und das, ohne einen Finger zu rühren. Wir kämpfen uns für dich durch den Tarifdschungel.</p>
    <p>Also spar' dir dein hart verdientes Geld und werde ein <strong>Voltwise</strong> Kunde.</p>
  </div>
  <a class="btn" href="#" style="left:150px;top:1064px">Jetzt Anmelden!</a>
  <div class="illus" role="img" aria-label="Illustration: Wegweiser in grüner Landschaft mit Sonne" style="left:670px;top:755px;width:300px;height:300px;border-radius:50%;background:linear-gradient(180deg,var(--sky) 0 45%,var(--teal) 45% 100%)"></div>
</section>

<section class="savings">
  <div class="illus" role="img" aria-label="Illustration: Stadt mit Häusern und Ersparnis-Plakette bis 850 Euro" style="left:150px;top:1245px;width:410px;height:265px;border-radius:130px;background:linear-gradient(180deg,var(--teal) 0 55%,#41464f 55% 100%)"></div>
  <h2 class="abs" style="left:635px;top:1206px">Die <span class="accent">günstigste</span> aller Superkräfte</h2>
  <div class="rule" style="left:635px;top:1260px"></div>
  <div class="copy abs" style="left:635px;top:1300px;width:420px">
    <p style="margin-bottom:8px">Ab 24 Euro bist du dabei</p>
    <ul>
      <li>Service für Strom oder Gas (1 Zähler): <strong>24 Euro/Jahr</strong></li>
      <li>Service für Strom und Gas (2 Zähler): <strong>36 Euro/Jahr</strong></li>
      <li>Die erste Gebühr verrechnen wir dir erst nach deinem <strong>ersten Wechsel</strong></li>
      <li><strong>Spare bis zu 850 Euro</strong> jährlich Strom- und Gaskosten beim 1. Wechsel*</li>
    </ul>
    <p class="note" style="margin-top:14px">* Jährliche Ersparnis eines durchschnittlichen Haushalts (3.500 kWh Strom und 15.000 kWh Gas) im Vergleich zum teuersten Anbieter, berechnet nach dem ersten Wechsel laut Tarifamt-Preisrechner vom 01.11.2018.</p>
  </div>
  <a class="btn" href="#" style="left:635px;top:1568px">Jetzt Anmelden!</a>
</section>

<section class="steps">
  <h2 class="center-title" style="top:1722px">Wie werde ich <span class="accent">Voltwise</span> Kunde?</h2>
  <div class="rule" style="left:525px;top:1790px"></div>
  <div class="steps-map" role="img" aria-label="Dezente Weltkarte aus Punkten"></div>
  <div class="step" style="left:150px"><span class="num">1.</span><h3>Einmalig<br>anmelden</h3><p>Jahresrechnung hochladen. Präferenzen auswählen. Anmeldung abschließen.</p></div>
  <div class="step" style="left:457px"><span class="num">2.</span><h3>Automatischer<br>Tarifwechsel</h3><p>Wir suchen den günstigsten Tarif für dich aus und führen den Wechsel automatisch durch.</p></div>
  <div class="step" style="left:764px"><span class="num">3.</span><h3>Zurücklehnen und<br>Geld sparen</h3><p>Immer automatisch zum günstigsten Tarif wechseln.</p></div>
</section>

<section class="benefits">
  <h2 class="center-title" style="top:2177px">Einmal anmelden, <span class="accent">immer sparen</span></h2>
  <div class="rule" style="left:525px;top:2235px"></div>

  <div class="feature" style="left:248px">
    <svg width="52" height="44" viewBox="0 0 52 44" aria-hidden="true"><path d="M2 20 50 2 38 42 24 28Z" fill="#bfe3ee"/><path d="M24 28 50 2 18 24 20 40Z" fill="#8fcadb"/></svg>
    <h4>UNABHÄNGIG</h4>
    <p>Wir arbeiten nur für dich. Um unabhängig zu bleiben, verzichten wir bewusst auf Provisions-Deals mit Energieanbietern.</p>
  </div>
  <div class="feature" style="left:532px">
    <svg width="72" height="44" viewBox="0 0 72 44" aria-hidden="true"><g fill="none" stroke="#f7c65a" stroke-width="7" stroke-dasharray="4 3"><circle cx="20" cy="28" r="11"/><circle cx="48" cy="14" r="9"/></g><circle cx="20" cy="28" r="5" fill="#f7c65a"/><circle cx="48" cy="14" r="4" fill="#f7c65a"/></svg>
    <h4>AUTOMATISCH</h4>
    <p>Du meldest dich einmal an und wir übernehmen den Rest. Ganz automatisch.</p>
  </div>
  <div class="feature" style="left:810px">
    <svg width="46" height="44" viewBox="0 0 46 44" aria-hidden="true"><rect x="10" y="2" width="22" height="16" rx="2" fill="#f7a823" transform="rotate(20 21 10)"/><rect x="2" y="14" width="40" height="28" rx="4" fill="#f59c7a"/><rect x="28" y="24" width="14" height="9" rx="2" fill="#f26a22"/></svg>
    <h4>FAIR</h4>
    <p>Bei Voltwise bleibt mehr im Börsel. Trotz Service-Gebühr.</p>
  </div>
</section>

<div class="cta">Haben Sie irgendwelche Fragen? Fühlen Sie sich frei uns zu kontaktieren! <a href="#">Kontaktiere uns!</a></div>

<footer class="footer">
  <div class="brand" style="left:150px;top:40px">Voltwise <span class="dot" style="background:var(--orange)"></span></div>
  <nav class="nav">
    <a class="active" href="#">So Funktionierts</a><a href="#">Preise</a><a href="#">Fragen?</a><a href="#">Über Uns</a><a href="#">Betriebe</a><a href="#">Erfahrungen</a><a href="#">Pressestimmen</a>
  </nav>
  <div class="social" aria-label="Soziale Netzwerke"><span></span><span></span><span></span><span></span><span></span></div>
  <div class="legal">AGB / DATENSCHUTZ / IMPRESSUM</div>
</footer>

</body>
</html>
```